Mobile phone signal boosting solutions needs a website

We need a website design for the reselling of a mobile signal boosting product set. These solutions are Vexlor exempt and will provide an indoor signal for mobile phones. We would like to see designs that incorporate the colours and feel of our logo. The domain will be
openmeadow.com / co.uk
Overview of the company and how it is to be used: Open meadow (domain name) will work with business and end user to provide mobile signal boosting – where people struggle indoors with a mobile signal our solutions will help by finding the smallest signal and boosting it, allowing users to use voice and data over their mobile network (please note this is not wireless signal boosting)
Number of Pages:
-Home
-Solutions / How it works
-Case Studies
-Contact
Text content: Currently just use placeholders
Technical specs : Wordpress and ability to use CMS if that’s relevant
Target Market(s)
Business professional all markets /high end residential
Coded - Design and coding required
4 page

```html
<!DOCTYPE html>
<html lang="en">
<head>
<meta charset="utf-8">
<title>Open Meadow – Mobile Signal Boosting</title>
<link href="https://fonts.googleapis.com/css2?family=Roboto:wght@400;500;700&family=Poppins:wght@400;500&display=swap" rel="stylesheet">
<style>
:root{
  --yellow:#fdc300;
  --orange:#f2a516;
  --ink:#111111;
  --text:#555555;
  --white:#ffffff;
  --footer:#0b0b0b;
  --hero-a:#2b2b2b;
  --hero-b:#141414;
}
*{margin:0;padding:0;box-sizing:border-box}
html,body{width:1200px;height:2726px;overflow:hidden;background:var(--white)}
body{font-family:'Roboto',sans-serif;color:var(--ink);position:relative}
.abs{position:absolute}
.center{left:0;width:1200px;text-align:center}

/* header */
.site-header{position:absolute;left:0;top:0;width:1200px;height:177px;background:var(--white)}
.brand{position:absolute;left:70px;top:72px;width:170px;text-align:center;font:500 30px/1 'Roboto',sans-serif;color:var(--ink);letter-spacing:-1px}
.contact-item{position:absolute;top:37px;display:flex;align-items:center;gap:12px;font:500 13px 'Roboto',sans-serif;color:#333}
.contact-icon{width:28px;height:28px;border-radius:50%;background:var(--yellow);display:flex;align-items:center;justify-content:center}
.socials{position:absolute;display:flex;gap:5px}
.social{width:39px;height:39px;background:var(--yellow)}
.main-nav{position:absolute;top:119px;left:0;width:1200px;font:500 13px 'Roboto',sans-serif;color:#333}
.main-nav span{position:absolute;transform:translateX(-50%)}
.main-nav .active{color:var(--yellow)}
.nav-line{position:absolute;left:312px;top:109px;width:148px;height:2px;background:var(--orange)}

/* hero */
.hero{position:absolute;left:0;top:177px;width:1200px;height:591px;background:linear-gradient(120deg,var(--hero-a),var(--hero-b) 60%,#2a2a2a)}
.hero-photo{position:absolute;right:0;top:0;width:400px;height:591px;background:radial-gradient(circle at 55% 55%,#3a3a3a,rgba(20,20,20,0) 70%)}
.hero h1{position:absolute;left:27px;top:250px;font:700 53px/62px 'Roboto',sans-serif;color:var(--white);letter-spacing:-0.5px}
.hero h1 .hl{color:var(--yellow)}
.btn{position:absolute;height:32px;background:var(--orange);color:var(--white);font:500 13px/32px 'Roboto',sans-serif;padding:0 19px;display:flex;align-items:center;gap:5px}

h2.section-title{font:500 32px 'Roboto',sans-serif;color:var(--ink)}
h2.section-title .hl{color:var(--yellow)}
.lead{font:400 14px/20px 'Poppins',sans-serif;color:var(--text)}

/* about */
.about-mark{left:196px;top:846px;width:370px;height:344px;background:linear-gradient(180deg,#fafafa,#f0f0f0);display:flex;align-items:center;justify-content:center;font:500 34px 'Roboto',sans-serif;color:var(--ink)}
.about-text{left:607px;top:876px;width:423px;text-align:justify;font:400 14px/20px 'Poppins',sans-serif;color:var(--text)}

/* how */
.feature{position:absolute;width:360px;text-align:center;transform:translateX(-50%)}
.feature h3{font:500 14.5px 'Roboto',sans-serif;color:var(--ink);margin-top:14px}
.feature p{font:400 12.5px 'Roboto',sans-serif;color:#555;margin-top:17px}

/* cases */
.case{position:absolute;width:215px;text-align:center}
.case-photo{width:183px;height:121px;border-radius:10px;margin:0 auto}
.case h3{font:500 15px/19px 'Roboto',sans-serif;color:var(--ink);margin-top:30px}
.case p{font:400 12px/19px 'Poppins',sans-serif;color:var(--text);margin-top:13px}

/* footer */
.site-footer{position:absolute;left:0;top:2311px;width:1200px;height:415px;background:var(--footer);color:var(--white)}
.footer-brand{top:88px;font:500 20px 'Roboto',sans-serif;color:var(--white)}
.footer-nav{top:168px;display:flex;justify-content:center;gap:31px;font:500 12.5px 'Roboto',sans-serif}
.footer-nav .active{color:var(--yellow)}
.footer-contact{top:212px;display:flex;justify-content:center;gap:16px;font:400 13px 'Roboto',sans-serif;align-items:center}
.footer-contact span{display:flex;align-items:center;gap:6px}
.copyright{top:327px;font:400 12.5px 'Roboto',sans-serif}
</style>
</head>
<body>

<header class="site-header">
  <div class="brand">Open Meadow</div>

  <div class="contact-item" style="left:310px">
    <span class="contact-icon"><svg width="14" height="14" viewBox="0 0 24 24"><path fill="#fff" d="M6.6 10.8a15 15 0 006.6 6.6l2.2-2.2a1 1 0 011-.25 11.4 11.4 0 003.6.6 1 1 0 011 1V20a1 1 0 01-1 1A17 17 0 013 4a1 1 0 011-1h3.5a1 1 0 011 1c0 1.25.2 2.45.6 3.6a1 1 0 01-.25 1z"/></svg></span>
    Call Us: +1 555 010 2030
  </div>
  <div class="contact-item" style="left:700px">
    <span class="contact-icon"><svg width="14" height="12" viewBox="0 0 24 20"><rect x="1" y="2" width="22" height="16" rx="2" fill="#fff"/><path d="M2 4l10 7 10-7" stroke="#fdc300" stroke-width="2" fill="none"/></svg></span>
    Mail Us: info@openmeadow.com
  </div>

  <div class="socials" style="left:1062px;top:36px">
    <div class="social" role="img" aria-label="Social profile link"></div>
    <div class="social" role="img" aria-label="Social profile link"></div>
    <div class="social" role="img" aria-label="Social profile link"></div>
  </div>

  <div class="nav-line"></div>
  <nav class="main-nav">
    <span class="active" style="left:386px">Home</span>
    <span style="left:544px">About Us</span>
    <span style="left:723px">How It Works</span>
    <span style="left:912px">Case Studies</span>
    <span style="left:1095px">Contact Us</span>
  </nav>
</header>

<section class="hero" role="img" aria-label="Dark geometric wall with a hand holding a phone showing strong signal waves">
  <div class="hero-photo"></div>
  <h1>We Provide Mobile Phone<br><span class="hl">Signal Boosting Solutions</span></h1>
  <a class="btn" style="left:256px;top:388px">Explore More <svg width="7" height="9" viewBox="0 0 7 10"><path d="M1 1l4 4-4 4" stroke="#fff" stroke-width="2" fill="none"/></svg></a>
</section>

<section class="about">
  <div class="abs about-mark" role="img" aria-label="Large brand mark">Open Meadow</div>
  <h2 class="abs section-title" style="left:607px;top:820px;width:423px;text-align:center">About <span class="hl">Us</span></h2>
  <p class="abs about-text">Lorem ipsum dolor sit amet, consectetur adipiscing elit, sed do eiusmod tempor incididunt ut labore et dolore magna aliqua. Tempor orci eu lobortis elementum nibh tellus molestie. Sagittis orci a scelerisque purus semper eget duis at. Commodo odio aenean sed adipiscing diam donec. Faucibus scelerisque eleifend donec pretium vulputate sapien. Cursus vitae congue mauris rhoncus aenean vel elit scelerisque mauris. Ultrices gravida dictum fusce ut placerat. Volutpat commodo sed egestas egestas fringilla phasellus faucibus. Mauris commodo quis imperdiet massa tincidunt. Sit amet justo donec enim diam vulputate. Mi eget mauris pharetra et ultrices neque. Vivamus arcu felis bibendum ut tristique et. Egestas maecenas pharetra convallis posuere morbi leo urna molestie at.</p>
  <a class="btn" style="left:608px;top:1162px">Explore More <svg width="7" height="9" viewBox="0 0 7 10"><path d="M1 1l4 4-4 4" stroke="#fff" stroke-width="2" fill="none"/></svg></a>
</section>

<section class="how">
  <h2 class="abs center section-title" style="top:1314px">How It <span class="hl">Works</span></h2>
  <p class="abs center lead" style="top:1367px">Lorem ipsum dolor sit amet, consectetur adipiscing elit, sed do eiusmod tempor incididunt ut labore et dolore magna aliqua.<br>Tempor orci eu lobortis elementum nibh tellus molestie.</p>

  <div class="feature" style="left:395px;top:1469px">
    <svg width="32" height="40" viewBox="0 0 32 40"><rect x="0" y="0" width="32" height="40" fill="#fdc300"/><g fill="#fff"><rect x="8" y="6" width="4" height="4"/><rect x="20" y="6" width="4" height="4"/><rect x="8" y="14" width="4" height="4"/><rect x="20" y="14" width="4" height="4"/><rect x="8" y="22" width="4" height="4"/><rect x="20" y="22" width="4" height="4"/><rect x="13" y="31" width="6" height="9"/></g></svg>
    <h3>In-Building Signal Boosters</h3>
    <p>Designed for homes, offices, and commercial buildings.</p>
  </div>
  <div class="feature" style="left:804px;top:1469px">
    <svg width="52" height="40" viewBox="0 0 52 40"><path d="M10 6h32l6 14v14H4V20z" fill="#fdc300"/><path d="M14 10h10v9H10zM28 10h10l4 9H28z" fill="#fff"/><circle cx="14" cy="32" r="6" fill="#fdc300" stroke="#fff" stroke-width="3"/><circle cx="38" cy="32" r="6" fill="#fdc300" stroke="#fff" stroke-width="3"/></svg>
    <h3>Vehicle Signal Boosters</h3>
    <p>Designed for cars, trucks, RVs, SUVs, boats, and fleet vehicles.</p>
  </div>

  <a class="btn" style="left:911px;top:1609px">Explore More <svg width="7" height="9" viewBox="0 0 7 10"><path d="M1 1l4 4-4 4" stroke="#fff" stroke-width="2" fill="none"/></svg></a>
</section>

<section class="cases">
  <h2 class="abs center section-title" style="top:1734px">Case <span class="hl">Studies</span></h2>
  <p class="abs center lead" style="top:1787px">Lorem ipsum dolor sit amet, consectetur adipiscing elit, sed do eiusmod tempor incididunt ut labore et dolore magna aliqua.<br>Tempor orci eu lobortis elementum nibh tellus molestie.</p>

  <article class="case" style="left:219px;top:1910px">
    <div class="case-photo" role="img" aria-label="Three colleagues talking around a table" style="background:linear-gradient(135deg,#4e5a4c,#b9aa98 60%,#3b3e3a)"></div>
    <h3>Nisl nunc mi ipsum faucibus vitae aliquet</h3>
    <p>Lorem ipsum dolor sit amet, consectetur adipiscing elit. Ut elit tellus, luctus nec ullamcorper mattis, pulvinar dapibus leo.</p>
  </article>
  <article class="case" style="left:493px;top:1910px">
    <div class="case-photo" role="img" aria-label="Man in a blue shirt using a phone in a shop" style="background:linear-gradient(120deg,#e9e4dc,#5d86c4 50%,#d19a3a)"></div>
    <h3>Id leo in vitae turpis massa sed</h3>
    <p>Lorem ipsum dolor sit amet, consectetur adipiscing elit. Ut elit tellus, luctus nec ullamcorper mattis, pulvinar dapibus leo.</p>
  </article>
  <article class="case" style="left:766px;top:1910px">
    <div class="case-photo" role="img" aria-label="Mobile phone mast against a blue sky" style="background:linear-gradient(160deg,#2f6fc9,#4a86d6)"></div>
    <h3>Commodo elit at imperdiet dui</h3>
    <p>Lorem ipsum dolor sit amet, consectetur adipiscing elit. Ut elit tellus, luctus nec ullamcorper mattis, pulvinar dapibus leo.</p>
  </article>

  <a class="btn" style="left:911px;top:2232px">Explore More <svg width="7" height="9" viewBox="0 0 7 10"><path d="M1 1l4 4-4 4" stroke="#fff" stroke-width="2" fill="none"/></svg></a>
</section>

<footer class="site-footer">
  <div class="abs center footer-brand">Open Meadow</div>
  <nav class="abs center footer-nav">
    <span class="active">Home</span><span>About Us</span><span>How It Works</span><span>Case Studies</span><span>Contact Us</span>
  </nav>
  <div class="abs center footer-contact">
    <span><svg width="15" height="12" viewBox="0 0 24 20"><rect x="1" y="2" width="22" height="16" rx="2" fill="#fdc300"/><path d="M2 4l10 7 10-7" stroke="#0b0b0b" stroke-width="2" fill="none"/></svg>Mail Us: info@openmeadow.com</span>
    <span><svg width="14" height="14" viewBox="0 0 24 24"><path fill="#fdc300" d="M6.6 10.8a15 15 0 006.6 6.6l2.2-2.2a1 1 0 011-.25 11.4 11.4 0 003.6.6 1 1 0 011 1V20a1 1 0 01-1 1A17 17 0 013 4a1 1 0 011-1h3.5a1 1 0 011 1c0 1.25.2 2.45.6 3.6a1 1 0 01-.25 1z"/></svg>call Us: +1 555 010 2030</span>
  </div>
  <div class="socials" style="left:537px;top:246px">
    <div class="social" role="img" aria-label="Social profile link"></div>
    <div class="social" role="img" aria-label="Social profile link"></div>
    <div class="social" role="img" aria-label="Social profile link"></div>
  </div>
  <p class="abs center copyright">Copyright © 2023 openmeadow | Powered by openmeadow</p>
</footer>

</body>
</html>
```